Information Technology Cloud Services Website

"Offer in every submission a high resolution version of your concept please. It is difficult to see of my text (sales copy) was added to your screenshot or not. It is necessary for me to provide high quality feedback."

My company provides a customizable ecosystem for Trelvane Workdesk 720 and Kolbrin users that includes all the technologies for organizing business processes and communications, letting my clients manage business without fear.

You can see our current site at http://www.720ShiftSpecialists.com

I currently use WordPress using the theme platform OptimizePress. If you have OptimizePress, that would be perfect, yet not required. However, I do need the finish product in WordPress for future additions and edits.

The Brand colors are Light Blue just like the logo attached.

I am in the need of graphic images on every webpage that can convey the services that my company does.

We need a refresh of our existing website that looks more 2018. We have made a mockup of the content that we want and a sample of where we want it. Nothing is set in stone, if you have better ideas of where things should go, feel free.

My instructions are inside the Word document named File 8: 720 Homepage Layout Monday, 22 January 2018 08:06:03

Here are some competitors similar sites we like - but still looking for a unique design that fits out brand

https://www.brovantech.com/

https://www.quorlymail.com/email-migrations/workdesk-720-shift-specialists

https://www.zendrofal.com/solutions/mailbox-migration/

https://www.plumacore.com/

https://www.plumacore.com/workdesk-720/

Target Market(s)

Business = IT Managers, IT Directors, IT Staff, IT Vice Presidents, Chief Information Officer

Industry/Entity Type

Information Technology

Coding

Coded - Design and coding required

Number of Pages Required

5+ page

Font styles to use
Sans Serif

Colors

Designer to choose colors to be used in the design.

Requirements
Must have
• Must have creative graphic images that convey the story/services that I offer. Its important to us that the design is very explanatory, the customer should easily be able to figure out that we provide Workdesk 720 migrations services right away. Also we are looking for a new very responsive HTML5+ webpages in WordPress.

```html
<!DOCTYPE html>
<html lang="en">
<head>
<meta charset="utf-8">
<title>720ShiftSpecialists – Cloud Migration</title>
<link rel="stylesheet" href="https://fonts.googleapis.com/css2?family=Open+Sans:wght@400;600;700;800&display=swap">
<style>
:root{
  --brand:#2fb6e9;
  --brand-dark:#1a8fc9;
  --ink:#3b3f45;
  --muted:#7a8089;
  --line:#e3e7ec;
  --soft:#f3f5f8;
  --seen:#2c2e33;
  --footer-deep:#1a1c20;
  --white:#ffffff;
}
*{box-sizing:border-box;margin:0;padding:0}
html,body{width:1200px;height:4737px;overflow:hidden}
body{font-family:"Open Sans",Arial,sans-serif;color:var(--ink);background:var(--white)}
section,header,footer{position:relative;width:1200px;overflow:hidden}
.btn{display:inline-block;padding:10px 22px;border-radius:3px;font-size:12px;font-weight:700;letter-spacing:.5px;text-transform:uppercase;color:var(--white);background:var(--brand)}
.btn-ghost{background:transparent;border:1px solid var(--white)}
.placeholder{position:absolute;inset:0}

/* hero */
.hero{height:673px;color:var(--white);text-align:center}
.hero .placeholder{background:linear-gradient(100deg,#3fc7c0 0%,#2fb0d8 45%,#2b7fd0 100%)}
.nav{position:absolute;top:0;left:0;right:0;height:52px;display:flex;align-items:center;padding:0 40px;z-index:2}
.logo{display:flex;align-items:center;gap:10px;font-size:14px;font-weight:700;color:var(--white)}
.logo-dot{width:26px;height:26px;border-radius:50%;background:var(--white);opacity:.9}
.menu{margin-left:auto;display:flex;gap:26px;font-size:11px;font-weight:600;align-items:center}
.menu .btn{padding:6px 14px;font-size:10px;border-radius:14px;background:var(--white);color:var(--brand-dark)}
.hero-copy{position:absolute;top:272px;left:0;right:0;z-index:2}
.hero h1{font-size:20px;font-weight:800;line-height:1.3;text-transform:uppercase;width:500px;margin:0 auto}
.hero p{font-size:11px;margin-top:8px;opacity:.9}
.hero .actions{margin-top:14px;display:flex;gap:12px;justify-content:center}
.hero .actions .btn{padding:7px 16px;font-size:10px}
.down{position:absolute;left:585px;top:625px;width:30px;height:30px;z-index:2}

/* seen in */
.seen{height:63px;background:var(--seen);display:flex;align-items:center;justify-content:center;gap:38px;color:var(--white)}
.seen em{font-style:italic;font-size:13px;font-weight:600;opacity:.8}
.seen span{font-size:16px;font-weight:800;letter-spacing:1px}

/* help */
.help{height:490px;text-align:center}
.intro{width:760px;margin:40px auto 0;font-size:11px;line-height:1.7;color:var(--muted);text-transform:uppercase}
.section-title{font-size:16px;font-weight:700;color:var(--brand-dark);margin-top:28px}
.cards{display:flex;gap:45px;justify-content:center;margin-top:30px}
.card{width:235px;height:270px;border:1px solid var(--line);box-shadow:0 2px 8px rgba(0,0,0,.06);padding:28px 22px}
.card .icon{width:56px;height:56px;margin:0 auto;border-radius:50%;background:linear-gradient(135deg,#4cc6f0,#f1b84a)}
.card h3{font-size:12px;font-weight:700;color:var(--brand-dark);margin-top:16px}
.card p{font-size:10.5px;line-height:1.7;color:var(--muted);margin-top:10px}

/* process */
.process{height:502px;background:var(--soft);text-align:center}
.process .section-title{margin-top:45px}
.sub{font-size:10.5px;color:var(--muted);text-transform:uppercase;margin-top:6px}
.diagram{position:absolute;left:0;top:60px}

/* bands */
.band{text-align:center;color:var(--white)}
.band .placeholder{background:linear-gradient(120deg,#2f8fd4,#36aee6 55%,#2b7cc4)}
.band-copy{position:absolute;left:0;right:0;z-index:2}
.band-1{height:430px}
.band-1 .band-copy{top:130px}
.band-1 h2{font-size:31px;font-weight:700;line-height:1.25;width:640px;margin:0 auto}
.band p{font-size:13px;margin-top:10px}
.band .btn{margin-top:20px;background:var(--brand-dark)}

/* why */
.why{height:676px;text-align:center}
.why .section-title{margin-top:50px}
.features{position:relative;height:220px;width:900px;margin:26px auto 0}
.feature{position:absolute;width:200px;text-align:center}
.feature .icon{width:38px;height:38px;margin:0 auto;border-radius:6px;background:linear-gradient(135deg,#f4b63f,#3fb8ec)}
.feature h4{font-size:12px;font-weight:700;color:var(--brand-dark);margin-top:8px;line-height:1.3}
.cols{display:flex;gap:40px;justify-content:center;margin-top:10px}
.col{width:250px;font-size:10px;line-height:1.7;color:var(--muted)}
.col.blue{background:var(--brand);color:var(--white);padding:14px;border-radius:3px}
.not-all{font-size:14px;font-weight:700;color:var(--ink);margin-top:36px}
.not-all-p{width:820px;margin:10px auto 0;font-size:10px;line-height:1.7;color:var(--muted)}

.band-2{height:525px}
.band-2 .band-copy{top:165px}
.band-2 h5{font-size:26px;font-weight:400}
.band-2 h2{font-size:17px;font-weight:700;line-height:1.6;width:680px;margin:10px auto 0}

/* migrate */
.migrate{height:275px;text-align:center}
.migrate .section-title{margin-top:30px}
.items{position:relative;width:900px;height:200px;margin:18px auto 0}
.item{position:absolute;width:220px}
.item .icon{width:40px;height:40px;margin:0 auto;border-radius:6px;background:linear-gradient(135deg,#2f8fe0,#55c4f2)}
.item h4{font-size:11.5px;font-weight:700;color:var(--brand-dark);margin-top:6px}
.item p{font-size:9.5px;color:var(--muted);margin-top:2px;line-height:1.45}

/* join */
.join{height:543px;background:var(--soft);text-align:center}
.join .section-title{margin-top:30px}
.quotes{display:flex;gap:48px;justify-content:center;margin-top:50px}
.quote{width:268px;height:430px;background:var(--brand);color:var(--white);padding:66px 24px 20px;position:relative;border-radius:2px}
.avatar{position:absolute;top:-28px;left:104px;width:60px;height:60px;border-radius:50%;border:3px solid var(--white);background:linear-gradient(135deg,#c9d4de,#8a98a8)}
.quote p{font-size:10.5px;line-height:1.8}
.quote .who{margin-top:18px;font-size:10.5px;font-weight:700}
.quote .role{font-size:9.5px;opacity:.85;margin-top:2px}

/* footer */
.contact{height:483px;color:var(--white)}
.contact .placeholder{background:linear-gradient(160deg,#2e3238,#202328)}
.contact-left{position:absolute;left:150px;top:70px;width:280px;font-size:12px;z-index:2}
.contact-row{display:flex;flex-direction:column;align-items:flex-start;gap:10px;margin-bottom:38px}
.contact-row strong{font-size:13px}
.contact-row span{font-size:10px;line-height:1.6;opacity:.8}
.contact-right{position:absolute;left:460px;top:55px;width:600px;text-align:center;z-index:2}
.contact-right h2{font-size:34px;font-weight:600}
.contact-right p{font-size:14px;margin-top:6px;opacity:.85;line-height:1.5}
.form{display:grid;grid-template-columns:1fr 1fr;gap:12px 16px;margin-top:40px;text-align:left}
.field{height:32px;background:var(--white);border-radius:2px;color:#8c9299;font-size:11px;padding:9px 12px}
.form .btn{grid-column:2;justify-self:end;background:var(--brand);font-size:11px;text-transform:none}
.bottom{height:77px;background:var(--footer-deep);display:flex;align-items:center;padding:0 60px;color:var(--white)}
.bottom .copy{margin:0 auto;font-size:10px;opacity:.55}
.social{display:flex;gap:8px}
.social i{width:18px;height:18px;border-radius:50%;background:var(--brand)}
</style>
</head>
<body>

<header class="hero">
  <div class="placeholder" role="img" aria-label="Team of IT staff working together in a bright office, tinted teal and blue"></div>
  <nav class="nav">
    <div class="logo"><i class="logo-dot"></i>720ShiftSpecialists</div>
    <div class="menu">
      <span>Workdesk 720 Migrations ▾</span>
      <span>Migration Services ▾</span>
      <span>Managing Your Workdesk 720 Needs ▾</span>
      <span>Marketing Services ▾</span>
      <span class="btn">Free Quote</span>
    </div>
  </nav>
  <div class="hero-copy">
    <h1>Are you willing to cut costs &amp; boost productivity by migrating your email server &amp; infrastructure to the cloud?</h1>
    <p>We help companies move to the cloud professionally, smoothly and without any downtime.</p>
    <div class="actions"><span class="btn">Request a Quote</span><span class="btn btn-ghost">Learn More</span></div>
  </div>
  <svg class="down" viewBox="0 0 30 30"><circle cx="15" cy="15" r="13" fill="none" stroke="#fff" stroke-width="2"/><path d="M9 12l6 6 6-6" fill="none" stroke="#fff" stroke-width="2"/></svg>
</header>

<section class="seen">
  <em>As Seen In:</em>
  <span>VEXA</span><span>ORBIT</span><span>TALLOW REPORT</span><span>LUMEN</span>
</section>

<section class="help">
  <p class="intro">When it comes to moving your email server and infrastructure to the cloud, you don't want to lose sleep or break your budget. All you need is to go with experienced teams who handle every step professionally and efficiently, down to every small detail.</p>
  <h2 class="section-title">Here's How 720ShiftSpecialists Can Help Your Business</h2>
  <div class="cards">
    <div class="card"><div class="icon" role="img" aria-label="Clock and rocket illustration"></div><h3>SAVE TIME</h3><p>Our team of experts handles the whole migration and plans every step, so your staff can keep working while we move data and settings behind the scenes and finish on schedule.</p></div>
    <div class="card"><div class="icon" role="img" aria-label="Gears illustration"></div><h3>SAVE EFFORT</h3><p>Stop wrestling with complex tools and long manuals. We take care of mailboxes, users, files and permissions so your IT department can stay focused on running the business day to day.</p></div>
    <div class="card"><div class="icon" role="img" aria-label="Coins and person illustration"></div><h3>SAVE MONEY</h3><p>Moving to the cloud removes costly servers and maintenance contracts. With flat pricing and no surprises, you pay only for what you need and keep your budget under control.</p></div>
  </div>
</section>

<section class="process">
  <h2 class="section-title">OUR MIGRATION PROCESS</h2>
  <p class="sub">At any time of the day or night, 24/7 &amp; 365 days out of the year</p>
  <svg class="diagram" width="1200" height="370" viewBox="0 0 1200 370" font-family="Open Sans, Arial, sans-serif">
    <path d="M330 185 H870" stroke="#8ea1b5" stroke-width="3" fill="none"/>
    <path d="M330 185 q-20 -40 20 -45" stroke="#8ea1b5" stroke-width="3" fill="none"/>
    <path d="M862 178 l14 7 -14 7z" fill="#8ea1b5"/>
    <g stroke="#8a96a3" stroke-width="2">
      <line x1="385" y1="70" x2="385" y2="150"/>
      <line x1="490" y1="220" x2="490" y2="310"/>
      <line x1="600" y1="70" x2="600" y2="150"/>
      <line x1="705" y1="220" x2="705" y2="310"/>
      <line x1="815" y1="70" x2="815" y2="150"/>
    </g>
    <g fill="#1f7fcf" stroke="#fff" stroke-width="4">
      <circle cx="385" cy="185" r="34"/><circle cx="490" cy="185" r="40"/><circle cx="600" cy="185" r="34"/><circle cx="705" cy="185" r="34"/><circle cx="815" cy="185" r="34"/>
    </g>
    <g fill="none" stroke="#fff" stroke-width="2.5">
      <path d="M373 177 a7 7 0 0 1 14 0 v14 h-14z"/><circle cx="390" cy="187" r="3"/>
      <path d="M478 185 h24 M490 173 v24"/>
      <path d="M588 180 h22 l-6 -6 M612 190 h-22 l6 6"/>
      <rect x="693" y="175" width="24" height="17" rx="2"/><path d="M699 197 h12"/>
      <path d="M804 186 l8 8 14 -16"/>
    </g>
    <g fill="#5c6773">
      <circle cx="385" cy="58" r="13"/><circle cx="490" cy="322" r="13"/><circle cx="600" cy="58" r="13"/><circle cx="705" cy="322" r="13"/><circle cx="815" cy="58" r="13"/>
    </g>
    <g fill="#fff" font-size="12" font-weight="700" text-anchor="middle">
      <text x="385" y="62">1</text><text x="490" y="326">2</text><text x="600" y="62">3</text><text x="705" y="326">4</text><text x="815" y="62">5</text>
    </g>
    <g fill="#3b3f45" font-size="12" font-weight="700" text-anchor="middle">
      <text x="285" y="245">First Contact</text>
      <text x="500" y="88">Pre-Migration</text>
      <text x="545" y="245">Start Migration</text>
      <text x="705" y="88">Local Setup</text>
      <text x="905" y="245">Post Migration</text>
    </g>
    <g fill="#8a9097" font-size="9" text-anchor="middle">
      <text x="285" y="262">We listen to your goals</text><text x="285" y="274">and review your setup</text>
      <text x="500" y="104">We plan accounts, data</text><text x="500" y="116">and a safe timeline</text>
      <text x="545" y="262">We move mailboxes</text><text x="545" y="274">and files securely</text>
      <text x="705" y="104">We configure devices</text><text x="705" y="116">and user profiles</text>
      <text x="905" y="262">We verify, support and</text><text x="905" y="274">train your team</text>
    </g>
  </svg>
</section>

<section class="band band-1">
  <div class="placeholder" role="img" aria-label="Business people meeting around a laptop, tinted blue"></div>
  <div class="band-copy">
    <h2>Did You Know? – Cloud Services Like Trelvane Workdesk 720 And Kolbrin Can Help You Boost Your Productivity?</h2>
    <p>Speak With One Of Our Expert Engineers About Your Business Goals</p>
    <span class="btn">Request a Quote Today</span>
  </div>
</section>

<section class="why">
  <h2 class="section-title">WHY CHOOSE 720SHIFTSPECIALISTS?</h2>
  <div class="features">
    <div class="feature" style="left:0;top:0"><div class="icon" role="img" aria-label="Price tag icon"></div><h4>Flat Rate Migration</h4></div>
    <div class="feature" style="left:350px;top:0"><div class="icon" role="img" aria-label="Support headset icon"></div><h4>Responsive<br>Support 24/7/365</h4></div>
    <div class="feature" style="left:700px;top:0"><div class="icon" role="img" aria-label="Contract document icon"></div><h4>No Annual Commitment<br>Contract on Licenses</h4></div>
    <div class="feature" style="left:170px;top:110px"><div class="icon" role="img" aria-label="Adjustable building blocks icon"></div><h4>Solutions Adapt to<br>your Needs</h4></div>
    <div class="feature" style="left:520px;top:110px"><div class="icon" role="img" aria-label="Team member icon"></div><h4>Professional<br>Dedicated Team</h4></div>
  </div>
  <div class="cols">
    <p class="col">You pay one simple price for your migration, agreed upfront. No hidden hours, no surprise invoices and no extra fees when your project grows a little bigger than planned.</p>
    <p class="col blue">You will have access to 24/7 support by phone, email or chat. Our engineers answer quickly and stay with you until every issue is fully solved, day or night.</p>
    <p class="col">We do not lock you into long contracts. You can add or remove licenses month by month and keep only the services your company really needs.</p>
  </div>
  <h3 class="not-all">AND THAT'S NOT ALL...</h3>
  <p class="not-all-p">Adding cloud services will give your company better security, simpler updates and lower costs. We will stand by your side before, during and after the move, so your team can enjoy all the benefits from the very first day.</p>
</section>

<section class="band band-2">
  <div class="placeholder" role="img" aria-label="Engineer working at a computer, tinted blue"></div>
  <div class="band-copy">
    <h5>Did You Know?</h5>
    <h2>720ShiftSpecialists Is The Most Cost-Effective &amp; Flexible Way To Do It?<br>What Are You Waiting For? Talk To An Expert NOW &amp; Get A FREE Evaluation!</h2>
    <span class="btn">Request a Quote Today</span>
  </div>
</section>

<section class="migrate">
  <h2 class="section-title">WHAT WE MIGRATE</h2>
  <div class="items">
    <div class="item" style="left:0;top:0"><div class="icon" role="img" aria-label="Directory sync icon"></div><h4>User Registry Synchronization</h4><p>No need to recreate your users or groups</p></div>
    <div class="item" style="left:340px;top:0"><div class="icon" role="img" aria-label="Mailbox icon"></div><h4>Mailboxes</h4><p>MailCore, IMAP and hosted mail<br>to Workdesk 720 mailboxes</p></div>
    <div class="item" style="left:680px;top:0"><div class="icon" role="img" aria-label="Cloud storage icon"></div><h4>Data Storage</h4><p>From storage to CloudDrawer storage</p></div>
    <div class="item" style="left:170px;top:100px"><div class="icon" role="img" aria-label="Shared documents icon"></div><h4>TeamVault</h4><p>From TeamVault to TeamVault<br>online</p></div>
    <div class="item" style="left:510px;top:100px"><div class="icon" role="img" aria-label="Tenant transfer icon"></div><h4>W720 to W720</h4><p>Moving from one tenant to another<br>for mergers and acquisitions</p></div>
  </div>
</section>

<section class="join">
  <h2 class="section-title">JOIN 1000'S OF PEOPLE BENEFITING FROM WORKDESK 720</h2>
  <div class="quotes">
    <div class="quote"><div class="avatar" role="img" aria-label="Customer portrait"></div><p>As a company, the shift was smooth and quick. The team planned every detail, kept us informed the whole time and our staff were back to work the very next morning without losing a single email or file.</p><p class="who">Client Name</p><p class="role">IT Director, Retail Group</p></div>
    <div class="quote"><div class="avatar" role="img" aria-label="Customer portrait"></div><p>We had a difficult setup with many offices and old servers. The engineers mapped everything first, answered all our questions and moved us to the cloud over one weekend. Support has been excellent ever since.</p><p class="who">Client Name</p><p class="role">Chief Information Officer</p></div>
    <div class="quote"><div class="avatar" role="img" aria-label="Customer portrait"></div><p>The price was clear from day one and there were no surprises. Our users got training and help desk access, and our monthly costs went down. I would recommend this team to any IT manager.</p><p class="who">Client Name</p><p class="role">IT Manager, Health Services</p></div>
  </div>
</section>

<footer class="contact">
  <div class="placeholder" role="img" aria-label="Dark city skyline background"></div>
  <div class="contact-left">
    <div class="contact-row">
      <svg width="28" height="28" viewBox="0 0 24 24"><path d="M6.6 10.8a15 15 0 0 0 6.6 6.6l2.2-2.2c.3-.3.7-.4 1-.2 1.1.4 2.3.6 3.6.6.6 0 1 .4 1 1V20c0 .6-.4 1-1 1A17 17 0 0 1 3 4c0-.6.4-1 1-1h3.5c.6 0 1 .4 1 1 0 1.3.2 2.5.6 3.6.1.3 0 .7-.2 1z" fill="none" stroke="#fff" stroke-width="1.4"/></svg>
      <strong>Toll Free: (800) 555 0142</strong>
    </div>
    <div class="contact-row">
      <svg width="24" height="30" viewBox="0 0 24 30"><path d="M12 2a9 9 0 0 0-9 9c0 7 9 17 9 17s9-10 9-17a9 9 0 0 0-9-9z" fill="none" stroke="#fff" stroke-width="1.5"/><circle cx="12" cy="11" r="3.5" fill="none" stroke="#fff" stroke-width="1.5"/></svg>
      <span>Harbor Ridge Consulting LLC, 418 Calloway Lane, Suite 210,<br>Westbrook, NY 10099</span>
    </div>
    <div class="contact-row">
      <svg width="28" height="22" viewBox="0 0 28 22"><rect x="1" y="1" width="26" height="20" rx="2" fill="none" stroke="#fff" stroke-width="1.5"/><path d="M1 2l13 10 13-10" fill="none" stroke="#fff" stroke-width="1.5"/></svg>
      <span>hello@720shiftspecialists.example</span>
    </div>
  </div>
  <div class="contact-right">
    <h2>Ready To Start Migrating?</h2>
    <p>Speak With One Of Our Expert Engineers About<br>Your Business Goals</p>
    <div class="form">
      <div class="field">First Name</div><div class="field">Last Name</div>
      <div class="field">Company Name</div><div class="field">Email Address</div>
      <div class="field">Phone</div><div class="field">Zip</div>
      <span class="btn">Talk with an Expert Today</span>
    </div>
  </div>
</footer>

<div class="bottom">
  <div class="logo"><i class="logo-dot"></i>720ShiftSpecialists</div>
  <p class="copy">© 2018 720ShiftSpecialists. All rights reserved.</p>
  <div class="social"><i></i><i></i><i></i><i></i></div>
</div>

</body>
</html>
```